Vira Glow - Letter Head

My company is a residential and commercial cleaning company , which is located in Abu Dhabi, UAE.
I am looking for a creative letterhead reflects the professional and reflects professionalism and send the feeling of relax and comfort.
The color which will be used it has to be selected carefully in prospective of colors psychological effects, so every color to be used should be for a reason.
Also, reflecting my company colors in an attractive way.
Regarding the information which it should contains, it has to show the address, contacts , telephones an, email address and website.
Also, my company logo is attached

```html
<!DOCTYPE html>
<html lang="en">
<head>
<meta charset="utf-8">
<title>Vira Glow – Letterhead</title>
<link rel="stylesheet" href="https://fonts.googleapis.com/css2?family=PT+Sans:wght@400;700&display=swap">
<style>
  :root {
    --backdrop: #f1f1f2;
    --paper: #ececee;
    --ink: #1e1e1e;
    --brand-blue: #1769b0;
    --brand-green: #8cc63f;
    --footer-blue: #0b68ad;
    --footer-text: #ffffff;
    --watermark: #e1e1e4;
    --signature: #c9d2e6;
  }
  * { box-sizing: border-box; margin: 0; padding: 0; }
  html, body {
    width: 1113px; height: 1200px; overflow: hidden;
    background: var(--backdrop);
    font-family: "PT Sans", sans-serif;
  }
  .letterhead {
    position: absolute; left: 214px; top: 100px;
    width: 716px; height: 1012px;
    background: var(--paper);
    overflow: hidden;
  }
  .brand {
    position: absolute; top: 50px; left: 0; width: 100%;
    display: flex; justify-content: center; align-items: center; gap: 14px;
  }
  .brand-name {
    font-size: 40px; font-weight: 700; color: var(--brand-blue); letter-spacing: -0.5px;
  }
  .brand-mark {
    width: 64px; height: 64px; border-radius: 50%;
    border: 4px solid var(--brand-green);
  }
  .watermark {
    position: absolute; left: 136px; top: 720px; width: 600px; height: 260px;
  }
  .watermark-name {
    position: absolute; left: 0; top: 0;
    font-size: 118px; font-weight: 700; line-height: 96px; color: var(--watermark);
  }
  .watermark-mark {
    position: absolute; left: 336px; top: 0; width: 240px; height: 240px;
    border-radius: 50%; border: 6px solid var(--watermark);
  }
  .letter {
    position: absolute; left: 83px; top: 210px; width: 543px; color: var(--ink);
  }
  .greeting { font-size: 21px; margin-bottom: 38px; }
  .body-copy p {
    font-size: 12.6px; line-height: 19.8px; text-align: justify; margin-bottom: 19.8px;
  }
  .closing {
    position: absolute; left: 550px; top: 655px; font-size: 13px; color: var(--ink);
  }
  .signature {
    position: absolute; left: 455px; top: 685px; width: 160px; height: 58px;
    border-radius: 30px; background: var(--signature); opacity: 0.6;
  }
  .contact-band {
    position: absolute; left: 0; bottom: 0; width: 100%; height: 50px;
    background: var(--footer-blue); color: var(--footer-text);
    display: flex; justify-content: center; align-items: center; gap: 21px;
    font-size: 15px; letter-spacing: 0.3px;
  }
</style>
</head>
<body>
  <main class="letterhead">
    <header class="brand">
      <span class="brand-name">Vira Glow</span>
      <span class="brand-mark"></span>
    </header>

    <div class="watermark" aria-hidden="true">
      <div class="watermark-name">Vira<br>&nbsp;&nbsp;Glow</div>
      <div class="watermark-mark"></div>
    </div>

    <section class="letter">
      <p class="greeting">Dear Mr. Harlow,</p>
      <div class="body-copy">
        <p>Lorem ipsum dolor sit amet, consectetur adipiscing elit. Donec orci purus, luctus vitae dignissim eu, iaculis sed purus. Vivamus faucibus, ipsum nec aliquet viverra, leo mauris condimentum ligula, sit amet sagittis enim ligula quis arcu. Nam egestas tortor id nisi porttitor mattis. In tortor ante, ultricies in suscipit a, tempus non massa. Vivamus et auctor mi. Fusce vel massa nulla. Phasellus nec eros mauris, et scelerisque orci.</p>
        <p>Donec malesuada orci vitae nulla accumsan porta a id massa. Quisque accumsan iaculis magna sit amet fringilla. Maecenas consequat, magna eget tincidunt semper, odio nibh rutrum mi, id feugiat ante nisi eu risus. Vestibulum nunc orci, rhoncus a placerat in, ultricies in mi. Cras mattis varius eros, vel fringilla nisi suscipit eget. Quisque scelerisque sagittis nulla at porttitor.</p>
        <p>Sed id augue vitae urna euismod commodo aliquet a quam. Pellentesque arcu velit, cursus et malesuada ut, consequat et diam. Nullam erat sem, rhoncus id ullamcorper vitae, rhoncus et arcu. In ultricies ultricies nulla, ut rutrum nisi iaculis at. Donec eu magna a metus ornare faucibus. Fusce aliquet faucibus ultricies. Morbi semper, est id tincidunt gravida, sem arcu adipiscing lacus, ac bibendum nulla leo eu purus. Quisque nec diam sed risus consectetur a ccumsan quis quis nibh. Vestibulum id purus lorem.</p>
      </div>
    </section>

    <p class="closing">Sincerely,</p>
    <div class="signature" role="img" aria-label="Handwritten signature of Sam Reyes"></div>

    <footer class="contact-band">
      <span>Web: viraglow.example</span>
      <span>E-mail: office@viraglow.example</span>
      <span>Tel: 555 0142</span>
    </footer>
  </main>
</body>
</html>
```